Unique business card design

Boutique coastal hotel suites - in need of clever stand out business card I have uploaded the logo that I had created through quill forge I want something that is clever and stands out from everyone else - 418 Brantwell Avenue Corwin Halvey 99571 phone or text 907 -581-6142 www.primemarrowbysuites.com

Target Market(s)

Men and woman

Industry/Entity Type

Boutique coastal hotel

Contact Information for Business Card

Marrowby Suites Corwin Halvey marrowby_suites@mailnest.net

Requirements
Must have
• Classy - clever -bold 907-581-6142 call or text

```html
<!DOCTYPE html>
<html lang="en">
<head>
<meta charset="utf-8">
<title>Marrowby Suites – Business Card</title>
<link href="https://fonts.googleapis.com/css2?family=Kanit:wght@500&family=Roboto:wght@400&display=swap" rel="stylesheet">
<style>
  :root {
    --stage: #2b2b2c;
    --navy: #2f4863;
    --navy-deep: #2a4059;
    --paper: #f1f1f1;
    --paper-shade: #e4e4e4;
    --red: #bf2c2b;
    --ink: #2c2c2c;
    --white: #f4f4f4;
  }
  * { margin: 0; padding: 0; box-sizing: border-box; }
  html, body { width: 1200px; height: 1138px; overflow: hidden; background: var(--stage); }
  .canvas { position: relative; width: 1200px; height: 1138px; }

  .card {
    position: absolute;
    width: 620px;
    height: 374px;
    border-radius: 16px;
    overflow: hidden;
  }

  /* Front */
  .card-front {
    left: 274px; top: 186px;
    background: linear-gradient(180deg, var(--navy) 0%, var(--navy-deep) 100%);
    display: flex; align-items: center; justify-content: center;
  }
  .brand-name {
    font-family: "Kanit", sans-serif;
    font-weight: 500;
    font-size: 44px;
    letter-spacing: 5px;
    color: var(--white);
    text-transform: uppercase;
    display: flex; align-items: center; gap: 18px;
  }
  .brand-mark { width: 26px; height: 26px; background: var(--red); }

  /* Back */
  .card-back {
    left: 276px; top: 608px;
    background: linear-gradient(180deg, var(--paper) 0%, var(--paper-shade) 100%);
  }
  .back-panel { position: absolute; inset: 0; }
  .edge-dot {
    position: absolute; left: -14px; top: 60px;
    width: 28px; height: 58px; border-radius: 50%;
    background: linear-gradient(180deg, var(--red), var(--navy));
  }
  .contact { position: absolute; left: 39px; top: 54px; font-family: "Roboto", sans-serif; color: var(--ink); }
  .contact-name {
    font-family: "Kanit", sans-serif; font-weight: 500;
    font-size: 26px; color: var(--red); line-height: 1.2;
  }
  .contact-role { font-size: 15.5px; margin-top: 2px; }
  .address { position: absolute; left: 39px; top: 198px; font-family: "Roboto", sans-serif; font-style: normal; font-size: 16px; line-height: 25px; color: var(--ink); }
  .links { position: absolute; left: 39px; top: 272px; list-style: none; font-family: "Roboto", sans-serif; font-size: 16px; color: var(--ink); }
  .links li { display: flex; align-items: center; height: 26px; }
  .links svg { width: 14px; height: 14px; margin-right: 18px; fill: var(--red); }

  .back-brand {
    position: absolute; left: 495px; top: 187px;
    transform: translate(-50%, -50%) rotate(90deg);
    white-space: nowrap;
    font-family: "Kanit", sans-serif; font-weight: 500;
    font-size: 30px; letter-spacing: 3px; color: var(--white);
    text-transform: uppercase;
  }
</style>
</head>
<body>
<main class="canvas">

  <section class="card card-front" aria-label="Card front">
    <div class="brand-name"><span class="brand-mark"></span>Marrowby Suites</div>
  </section>

  <section class="card card-back" aria-label="Card back">
    <svg class="back-panel" viewBox="0 0 620 374" preserveAspectRatio="none">
      <path d="M400 0 Q 300 187 396 374" fill="none" stroke="var(--red)" stroke-width="12"/>
      <path d="M410 0 Q 318 187 406 374 L620 374 L620 0 Z" fill="var(--navy)"/>
    </svg>
    <div class="edge-dot"></div>

    <div class="contact">
      <h1 class="contact-name">Corwin Halvey</h1>
      <p class="contact-role">Managing Director</p>
    </div>

    <address class="address">
      418 Brantwell Avenue<br>
      Tarnholm, Alaska 99571
    </address>

    <ul class="links">
      <li><svg viewBox="0 0 16 16"><path d="M2 6c0-2 2-3 6-3s6 1 6 3l-3 1-1-2H6L5 7 2 6zM4 8h8l2 6H2l2-6zm4 1.5a2 2 0 100 4 2 2 0 000-4z"/></svg>(907) 581-6142</li>
      <li><svg viewBox="0 0 16 16"><path d="M1 3h14v10H1zM2 4.5v7.5l4.5-4zM14 4.5v7.5l-4.5-4zM2.5 4L8 8.8 13.5 4z"/></svg>marrowby_suites@mailnest.net</li>
      <li><svg viewBox="0 0 16 16"><path d="M8 1a7 7 0 100 14A7 7 0 008 1zm0 1.5c.8 1 1.3 2.2 1.5 3.5h-3C6.7 4.7 7.2 3.5 8 2.5zM2.6 7h2.9c0 .7 0 1.3.1 2H2.6a5.6 5.6 0 010-2zm3.9 0h3v2h-3zm4 0h2.9a5.6 5.6 0 010 2h-2.9c.1-.7.1-1.3 0-2zM6.5 10h3C9.3 11.3 8.8 12.5 8 13.5c-.8-1-1.3-2.2-1.5-3.5z"/></svg>primemarrowbysuites.com</li>
    </ul>

    <div class="back-brand">Marrowby Suites</div>
  </section>

</main>
</body>
</html>
```